Business Card Design

Maple Crest Rentals
Maple Crest Rentals is a high end home rental leasing company that provides exquisite properties in niche markets. We are a small family owned business that considers our clients not as renters, but as friends. Every property we buy must be brought up to our high standards before it is offered on the market. The properties that we lease are exceptional, "move in" ready homes. This allows for the client to take pride in their lease as if it was their own home. To put it another way; we do not lease a property that we would not live in ourselves.

Target Market(s)

Couples making $100K or more

Industry/Entity Type

Business

Requirements
Must have
• Some sort of logo
Nice to have
• good slogan
Should not have
• Pink

```html
<!DOCTYPE html>
<html lang="en">
<head>
<meta charset="utf-8">
<title>Maple Crest Rentals — Business Card</title>
<link rel="stylesheet" href="https://fonts.googleapis.com/css2?family=Ubuntu:wght@400;500;700&display=swap">
<style>
  :root {
    --backdrop: #e9ebee;
    --card: #ffffff;
    --brand-green: #009b6c;
    --ink: #222222;
    --ink-soft: #444444;
    --brand-maroon: #7a1f12;
  }
  html, body {
    margin: 0;
    padding: 0;
    width: 1200px;
    height: 1000px;
    overflow: hidden;
    background: var(--backdrop);
    font-family: "Ubuntu", sans-serif;
  }
  .canvas {
    position: relative;
    width: 1200px;
    height: 1000px;
  }
  .business-card {
    position: absolute;
    left: 100px;
    top: 210px;
    width: 1000px;
    height: 580px;
    background: var(--card);
    box-shadow: 0 6px 24px rgba(0, 0, 0, 0.15);
    overflow: hidden;
  }
  .contact-panel {
    position: absolute;
    left: 0;
    top: 0;
    width: 540px;
    height: 580px;
  }
  .stripe-green { fill: var(--brand-green); }
  .stripe-white { fill: var(--card); }
  .holder-name {
    font-family: "Ubuntu", sans-serif;
    font-weight: 700;
    font-size: 30px;
    fill: var(--ink-soft);
  }
  .holder-title {
    font-family: "Ubuntu", sans-serif;
    font-weight: 400;
    font-size: 17px;
    fill: var(--ink-soft);
  }
  .contact-line {
    font-family: "Ubuntu", sans-serif;
    font-weight: 500;
    font-size: 22px;
    fill: var(--ink);
  }
  .brand-block {
    position: absolute;
    left: 540px;
    right: 0;
    top: 0;
    bottom: 0;
    display: flex;
    align-items: center;
    justify-content: center;
    gap: 14px;
  }
  .brand-square {
    width: 26px;
    height: 26px;
    background: var(--brand-green);
  }
  .brand-name {
    font-family: "Ubuntu", sans-serif;
    font-weight: 700;
    font-size: 34px;
    color: var(--brand-maroon);
    letter-spacing: 0.5px;
  }
</style>
</head>
<body>
<main class="canvas">
  <section class="business-card">
    <svg class="contact-panel" viewBox="0 0 540 580" width="540" height="580">
      <defs>
        <clipPath id="panel-clip">
          <rect x="0" y="0" width="540" height="580"/>
        </clipPath>
      </defs>
      <g clip-path="url(#panel-clip)">
        <g transform="rotate(-25 270 290)">
          <rect class="stripe-green" x="-500" y="-400" width="1500" height="560"/>
          <rect class="stripe-white" x="-500" y="160" width="1500" height="90"/>
          <rect class="stripe-green" x="-500" y="250" width="1500" height="50"/>
          <rect class="stripe-white" x="-500" y="300" width="1500" height="62"/>
          <rect class="stripe-green" x="-500" y="362" width="1500" height="24"/>
          <rect class="stripe-white" x="-500" y="386" width="1500" height="60"/>
          <rect class="stripe-green" x="-500" y="446" width="1500" height="24"/>
          <rect class="stripe-white" x="-500" y="470" width="1500" height="60"/>
          <rect class="stripe-green" x="-500" y="530" width="1500" height="500"/>

          <text class="holder-name" x="300" y="208" text-anchor="middle">Your Name</text>
          <text class="holder-title" x="360" y="234" text-anchor="middle">Title</text>
          <text class="contact-line" x="495" y="340" text-anchor="end">Phone : 123- 456- 7890</text>
          <text class="contact-line" x="470" y="424" text-anchor="end">E-mail : yourname@mail.com</text>
          <text class="contact-line" x="435" y="508" text-anchor="end">Website : www.address.com</text>
        </g>
      </g>
    </svg>

    <div class="brand-block">
      <span class="brand-square" aria-hidden="true"></span>
      <span class="brand-name">Maple Crest Rentals</span>
    </div>
  </section>
</main>
</body>
</html>
```